Tranquil Pathway Business Card

Logo attached. (will be printing onto thick white/off white textured card)

Double sided business card for two Therapists working at Tranquil Pathway.

Require one design, but with different name and mobile numbers on each card.

Target Market(s)

Medical, Health

Industry/Entity Type

Business

Contact Information for Business Card

Need one business card design, but a separate card for each person - Colin Marchetti and Marieke de Boeckx.

FRONT OF CARD

Logo

Name (Colin Marchetti on one card, Marieke de Boeckx on the other)
Professional Clinical Hypnotherapist

Consulting Rooms (Near Lindqvist Hospital)
482 Brackenfield Road
Dunmore VIC 3987

Colin@TranquilPathway.example.au OR Marieke@TranquilPathway.example.au

Mobile: 0455 872 604 (for Colin) OR
Mobile: 0467 290 518 (for Marieke)

BACK OF CARD

Logo

Website: www.TranquilPathway.example.au

Phone: 1300 958 471

Requirements
Must have
• Text and logo only. No additiional graphics.

```html
<!DOCTYPE html>
<html lang="en">
<head>
<meta charset="utf-8">
<title>Tranquil Pathway – Business Card Back</title>
<link rel="stylesheet" href="https://fonts.googleapis.com/css2?family=Montserrat:wght@600;700&family=Open+Sans:wght@700&display=swap">
<style>
  :root {
    --navy: #222b5f;
    --grey: #6b6b6b;
    --frame: #3a3a3a;
    --paper: #ffffff;
  }
  * { margin: 0; padding: 0; box-sizing: border-box; }
  html, body {
    width: 1200px;
    height: 688px;
    overflow: hidden;
    background: var(--paper);
  }
  .card {
    position: relative;
    width: 1200px;
    height: 688px;
    background: var(--paper);
    border: 2px solid var(--frame);
  }
  .brand-mark {
    position: absolute;
    left: 291px;
    top: 222px;
    width: 198px;
    height: 198px;
  }
  .brand-name {
    position: absolute;
    left: 528px;
    top: 262px;
    font-family: "Montserrat", sans-serif;
    font-weight: 700;
    font-size: 52px;
    line-height: 1.1;
    letter-spacing: 1px;
    text-transform: uppercase;
    color: var(--navy);
  }
  .contact {
    position: absolute;
    left: 531px;
    top: 560px;
    font-family: "Open Sans", sans-serif;
    font-weight: 700;
    color: var(--navy);
  }
  .contact .website {
    font-size: 23px;
    font-variant: small-caps;
    letter-spacing: 0.3px;
    line-height: 30px;
  }
  .contact .phone {
    font-size: 28px;
    line-height: 36px;
  }
</style>
</head>
<body>
  <div class="card">
    <svg class="brand-mark" viewBox="0 0 198 198" aria-hidden="true">
      <circle cx="99" cy="99" r="99" fill="var(--navy)"/>
    </svg>
    <div class="brand-name">Tranquil<br>Pathway</div>
    <div class="contact">
      <p class="website">www.TranquilPathway.example.au</p>
      <p class="phone">1300 958 471</p>
    </div>
  </div>
</body>
</html>
```